Web site for small printshop

I am looking for a website for small printshop in Iceland, mainly serving university students and artist.

We print posters, flyers, business cards and more.

In addition to our current website, I would like to include design tool, (fx. www.quarlitune.example, www.dravonpix.example or something similar) jobs upload, shopping chart.
Updates

Great work, I am really amazed of the quality of work i am seeing here.

Really way beyond my expectation

GOOD JOB - all of you ! 

Hi all.

The designs submitted have been great, way better than expected.
I really did not expect this level of quality.

Some have been asking me for feedback on their designs, and I will try 
to send some feedback here, without spoiling your creativity.

Likes:
- when the colors of my logo is used in menus, buttons etc.
- simple, not to crowded look.

Dislikes.
- Dark and heavy design
- Lot of text and buttons (crowded look)

Extra info.
- top line (before menus) will contain: Tel - email - language
- menu line will have 5 categories: Home - service - submission of works - FAQ - about us
- 3 large buttons:  Job submit - Job design - ask for offer

LOVE YOUR WORK - great designs so far :)

Target Market(s)

University Students, Artists. Age group 20-30

Industry/Entity Type

University

Requirements
Must have
• The website must be easy to use, clean looking.

```html
<!DOCTYPE html>
<html lang="en">
<head>
<meta charset="utf-8">
<title>Víkurprent – Our Services</title>
<link href="https://fonts.googleapis.com/css2?family=Ubuntu:wght@400;500;700&family=Oswald:wght@300&family=Arimo&display=swap" rel="stylesheet">
<style>
:root{
  --red:#e8392f;
  --green:#1a9a4a;
  --yellow:#f7e52a;
  --lime:#7cc142;
  --ink:#333333;
  --text:#555555;
  --muted:#888888;
  --topbar:#f5f5f5;
  --band:#e2e2e2;
  --panel:#f7f7f7;
  --panel-line:#dddddd;
  --footer:#3d3b3c;
  --footer-text:#cfcfcf;
  --base:#141414;
  --base-text:#9a9a9a;
  --white:#ffffff;
}
*{margin:0;padding:0;box-sizing:border-box}
html,body{width:1200px;height:903px;overflow:hidden;background:var(--white)}
body{position:relative;font-family:"Ubuntu",sans-serif;color:var(--ink)}
.topbar{position:absolute;left:0;top:0;width:1200px;height:29px;background:var(--topbar);font-size:11.5px;font-weight:500}
.topbar-items{position:absolute;right:173px;top:7px;display:flex;gap:8px;align-items:center}
.topbar .call{color:var(--red)}
.topbar .mail{color:var(--green)}
.topbar .lang{color:var(--muted)}
.topbar .sep{width:2px;height:14px;background:var(--ink)}
.brand{position:absolute;left:171px;top:41px;display:flex;align-items:center;gap:8px}
.brand-mark{width:33px;height:43px;background:var(--red)}
.brand-name{font-size:27px;font-weight:700;color:var(--ink);letter-spacing:.2px}
.main-nav{position:absolute;left:561px;top:54px;display:flex;font-size:16px;font-weight:700;color:#555}
.main-nav a{color:inherit;text-decoration:none}
.main-nav .n1{margin-right:48px}.main-nav .n2{margin-right:35px}.main-nav .n3{margin-right:43px}.main-nav .n4{margin-right:40px}
.hero-title{position:absolute;left:173px;top:137px;font-family:"Oswald",sans-serif;font-weight:300;font-size:28px;line-height:30px;color:#555}
.hero-photo{position:absolute;left:629px;top:93px;width:325px;height:165px;background:linear-gradient(180deg,#ffffff 0%,#e9d7c6 45%,#8b6a58 100%);border-radius:120px 120px 0 0}
.band{position:absolute;left:0;top:258px;width:1200px;height:43px;background:var(--band);border-top:1px solid #d4d4d4}
.band h1{position:absolute;left:171px;top:10px;font-size:20px;font-weight:400;color:#222}
.copy{position:absolute;left:172px;top:328px;width:607px;font-size:11.2px;line-height:17.1px;color:var(--text);text-align:justify}
.copy p{margin-bottom:11px}
.actions{position:absolute;left:838px;top:310px;width:180px;height:447px;background:var(--panel);border:1px solid var(--panel-line)}
.action{position:absolute;left:0;width:180px;text-align:center;font-size:15.5px;font-weight:500;color:#222}
.action svg{display:block;margin:0 auto 8px}
.a1{top:16px}.a2{top:160px}.a3{top:314px}
.footer{position:absolute;left:0;top:770px;width:1200px;height:75px;background:var(--footer)}
.footer-brand{position:absolute;left:160px;top:22px;display:flex;align-items:center;gap:7px}
.footer-brand .mark{width:29px;height:37px;background:#9a9a9a}
.footer-brand .name{font-size:23px;font-weight:700;color:#8d8d8d}
.footer-nav{position:absolute;left:568px;top:29px;font-family:"Arimo",sans-serif;font-size:12.5px;color:var(--footer-text);display:flex}
.footer-nav span{margin-right:30px}
.footer-nav .f3{margin-right:18px}
.base{position:absolute;left:0;top:845px;width:1200px;height:58px;background:var(--base)}
.base p{position:absolute;left:160px;top:27px;font-family:"Arimo",sans-serif;font-size:10.5px;color:var(--base-text)}
</style>
</head>
<body>
<header>
  <div class="topbar">
    <div class="topbar-items">
      <span class="call">CALL US&nbsp;: 05 7788210</span><span class="sep"></span>
      <span class="mail">Mailto : hello@vikurprent.example</span><span class="sep"></span>
      <span class="lang">Language: English</span>
    </div>
  </div>
  <div class="brand"><span class="brand-mark"></span><span class="brand-name">VÍKURPRENT</span></div>
  <nav class="main-nav">
    <a class="n1" href="#">Home</a><a class="n2" href="#">Services</a><a class="n3" href="#">Submit Works</a><a class="n4" href="#">FAQ</a><a href="#">About us</a>
  </nav>
  <h2 class="hero-title">Want to reduce your print costs<br>and Productivity ?</h2>
  <div class="hero-photo" role="img" aria-label="Photo of a group of smiling young students"></div>
</header>
<section class="band"><h1>Our Services</h1></section>
<main class="copy">
  <p>Lorem Ipsum is simply dummy text of the printing and typesetting industry. Lorem Ipsum has been the industry's standard dummy text ever since the 1500s, when an unknown printer took a galley of type and scrambled it to make a type specimen book. It has survived not only five centuries, but also the leap into electronic typesetting, remaining essentially unchanged. It was popularised in the 1960s with the release of Stafmark sheets containing Lorem Ipsum passages, and more recently with desktop publishing software like Brenna PageForge including versions of Lorem Ipsum.</p>
  <p>It has survived not only five centuries, but also the leap into electronic typesetting, remaining essentially unchanged. It was popularised in the 1960s with the release of Stafmark sheets containing Lorem Ipsum passages, and more recently with desktop publishing software like Brenna PageForge including versions of Lorem Ipsum.</p>
  <p>It has survived not only five centuries, but also the leap into electronic typesetting, remaining essentially unchanged. It was popularised in the 1960s with the release of Stafmark sheets containing Lorem Ipsum passages, and more recently with desktop publishing software like Brenna PageForge including versions of Lorem Ipsum.</p>
</main>
<aside class="actions">
  <div class="action a1">
    <svg width="84" height="84" viewBox="0 0 84 84"><circle cx="42" cy="42" r="42" fill="var(--red)"/><rect x="24" y="33" width="36" height="25" rx="2" fill="#fff"/><rect x="35" y="26" width="14" height="9" rx="2" fill="none" stroke="#fff" stroke-width="3"/></svg>
    JOB SUBMIT
  </div>
  <div class="action a2">
    <svg width="84" height="84" viewBox="0 0 84 84"><circle cx="42" cy="42" r="42" fill="var(--yellow)"/><path d="M22 44c0-11 10-18 22-17 12 1 19 9 17 15-2 5-9 3-11 7-2 4 2 8-5 9-12 1-23-4-23-14z" fill="#3a3a3a"/><circle cx="32" cy="42" r="3" fill="var(--yellow)"/><circle cx="40" cy="35" r="3" fill="var(--yellow)"/><circle cx="50" cy="35" r="3" fill="var(--yellow)"/><circle cx="36" cy="50" r="3" fill="var(--yellow)"/></svg>
    JOB DESIGN
  </div>
  <div class="action a3">
    <svg width="84" height="84" viewBox="0 0 84 84"><circle cx="42" cy="42" r="42" fill="var(--lime)"/><path d="M30 33c0-8 6-13 13-13s13 5 13 12c0 9-10 9-10 17v2" fill="none" stroke="#fff" stroke-width="8" stroke-linecap="round"/><circle cx="46" cy="63" r="5" fill="#fff"/></svg>
    ASK FOR OFFER
  </div>
</aside>
<footer>
  <div class="footer">
    <div class="footer-brand"><span class="mark"></span><span class="name">VÍKURPRENT</span></div>
    <nav class="footer-nav"><span>Home</span><span>Quote Request</span><span class="f3">About us</span><span>Supplying your artwork</span><span>Contact Us</span></nav>
  </div>
  <div class="base"><p>Copyright @ 2012 www.lindavefur.example&nbsp; Privacy Policy | Disclaimer | Resources</p></div>
</footer>
</body>
</html>
```